Simple elegant feminine design - Going out on my own as a Mortgage Broker.
My thoughts are the following details on the Front, middle of the card possibly? Phone and email smaller font than my name?
Marnie Veltrin
Finance Specialist
p: 0438 215 962
e: marnie@veltrinlending.com.au
Bottom of the card
residential / commercial / equipment
I would like the Font in Rose Gold maybe white or black background? or Possibly a stone grey - are you able to do a few options? I'd like them embossed
Then I had an idea as a simple logo as per the attached if you get the idea in my scribble, my initials, capital M attached to a small v that leads/follows into a circle? Thicker Font In Rose Gold, middle of the card at the back.
Very open to ideas though and what colour you think would look better with the Rose Gold.
Thanks so much for your help, I am not very creative and savvy with this stuff :-)
Industry/Entity Type
Finance
Contact Information for Business Card
Marnie Veltrin
p: 0438 215 962
Look and feel

```html
<!DOCTYPE html>
<html lang="en">
<head>
<meta charset="utf-8">
<title>Marnie's Business Cards</title>
<link href="https://fonts.googleapis.com/css2?family=Ubuntu:wght@300;400&display=swap" rel="stylesheet">
<style>
  :root {
    --paper: #ffffff;
    --sheet-line: #222222;
    --stone: #060708;
    --rose: #f19ca9;
    --rose-icon: #e98c80;
    --vein-warm: #3a1a1c;
    --vein-pink: #2a0f1c;
  }
  * { box-sizing: border-box; margin: 0; padding: 0; }
  html, body { width: 998px; height: 1200px; overflow: hidden; background: var(--paper); }
  body { font-family: "Ubuntu", sans-serif; position: relative; }

  .sheet {
    position: absolute; inset: 1px;
    border: 1px solid var(--sheet-line);
  }
  .card {
    position: absolute; left: 64px; width: 879px;
    overflow: hidden;
  }
  .card--front { top: 41px; height: 532px; }
  .card--back  { top: 611px; height: 531px; }

  .card__stone {
    position: absolute; inset: 0;
    background:
      radial-gradient(ellipse at 90% 70%, var(--vein-warm) 0%, transparent 45%),
      radial-gradient(ellipse at 10% 85%, var(--vein-warm) 0%, transparent 40%),
      radial-gradient(ellipse at 40% 5%, var(--vein-pink) 0%, transparent 35%),
      var(--stone);
  }

  .frame {
    position: absolute; left: 52px; top: 63px; width: 775px; height: 419px;
    border: 14px solid var(--rose);
    background: var(--stone);
    color: var(--rose);
    text-align: center;
  }
  .contact-name {
    position: absolute; left: 0; right: 0; top: 36px;
    font-weight: 400; font-size: 52px; line-height: 1;
  }
  .contact-name__rule {
    position: absolute; left: 206px; width: 332px; top: 109px;
    height: 3px; background: var(--rose);
  }
  .contact-role {
    position: absolute; left: 0; right: 0; top: 120px;
    font-weight: 300; font-size: 34px; line-height: 1;
  }
  .contact-line {
    position: absolute; left: 0; right: 0;
    display: flex; justify-content: center; align-items: center; gap: 14px;
    font-weight: 300; font-size: 37px; line-height: 1;
  }
  .contact-line--phone { top: 236px; }
  .contact-line--email { top: 282px; }
  .contact-line svg { width: 30px; height: 30px; flex: none; }
  .services {
    position: absolute; left: 0; right: 0; top: 336px;
    font-weight: 300; font-size: 27px; letter-spacing: 0.5px; word-spacing: 4px;
  }

  .seal {
    position: absolute; left: 243px; top: 77px; width: 376px; height: 376px;
    border: 7px solid var(--rose); border-radius: 50%;
    background: var(--stone);
    display: flex; align-items: center; justify-content: center;
  }
  .seal__name {
    color: var(--rose); font-weight: 400; font-size: 40px; text-align: center; line-height: 1.2;
  }
</style>
</head>
<body>
  <div class="sheet"></div>

  <section class="card card--front">
    <div class="card__stone" role="img" aria-label="Black marble texture with rose gold and pink veins"></div>
    <div class="frame">
      <h1 class="contact-name">Marnie Veltrin</h1>
      <div class="contact-name__rule"></div>
      <p class="contact-role">Finance Specialist</p>
      <p class="contact-line contact-line--phone">
        <svg viewBox="0 0 30 30" aria-hidden="true">
          <circle cx="15" cy="15" r="15" fill="var(--rose-icon)"/>
          <path d="M11 8c1 0 2 3 2 4s-1 1-1 2 2 4 3 4 1-1 2-1 4 1 4 2-2 3-3 3C12 22 8 16 8 11c0-1 2-3 3-3z" fill="#fff"/>
        </svg>
        <span>0438 215 962</span>
      </p>
      <p class="contact-line contact-line--email">
        <svg viewBox="0 0 30 30" aria-hidden="true">
          <circle cx="15" cy="15" r="15" fill="var(--rose-icon)"/>
          <rect x="8" y="10" width="14" height="10" fill="#fff"/>
          <path d="M8 10l7 6 7-6" fill="none" stroke="var(--rose-icon)" stroke-width="1.5"/>
        </svg>
        <span>marnie@veltrinlending.com.au</span>
      </p>
      <p class="services">residential / commercial / equipment</p>
    </div>
  </section>

  <section class="card card--back">
    <div class="card__stone" role="img" aria-label="Black marble texture with rose gold and pink veins"></div>
    <div class="seal">
      <p class="seal__name">Marnie<br>Veltrin</p>
    </div>
  </section>
</body>
</html>
```